Mobile Home Page Design for “Zarvo for Plumbers” – in Figma

PipeDashly: Fast, Reliable Emergency Plumbing at Your Fingertips

PipeDashly is a streamlined platform connecting homeowners with trusted, local plumbers for urgent repairs—whether it’s a burst pipe, leak, or blocked toilet. Designed for speed and peace of mind, our homepage will be clean, modern, and mobile-optimized to guide users from problem to solution in minutes.

Our primary users are homeowners in stressful situations who care most about price transparency and how fast help can arrive. Bookings are made exclusively online, so the user experience must instill confidence and eliminate hesitation.

The call-to-action should be immediate and persuasive—"See Prices & Book" will be prominently featured as the main CTA. Additional trust-builders could include:

A simple 3-step booking illustration (Tell us what’s wrong → See prices → Get a plumber)
Customer reviews or “Trusted by 10,000+ homeowners” badges

Display real-time availability ("Next plumber available in 40 minutes")
Price estimates upfront—with clear service types

Target Market(s)

Home Owners: 35-65 Years old.

Industry/Entity Type

Home Services.

Number of Pages Required

1 page

Font styles to use
Sans Serif

Colors
0054AA
0677BA
7BADD7
CADEEF
E8F1F8
FFF300
FFF600
FEFA6F
FFFEC7
FFFEE8

Requirements
Nice to have
• Map showing that plumbers are nearby. Trustworthy look and feel. Blue/Red or Blue/Yellow.

```html
<!DOCTYPE html>
<html lang="en">
<head>
<meta charset="utf-8">
<title>PipeDashly – Mobile Screens</title>
<link href="https://fonts.googleapis.com/css2?family=Inter:wght@400;500;600;700&family=Orbitron:wght@500;600&display=swap" rel="stylesheet">
<style>
:root{
  --canvas:#f2f2f2;
  --ink:#1a1a1a;
  --muted:#555b63;
  --blue:#0054AA;
  --blue-2:#0677BA;
  --blue-soft:#CADEEF;
  --yellow:#F9C930;
  --white:#ffffff;
  --line:#d9dde2;
  --night:#0c0c0c;
  --map:#232b38;
  --star:#F7B500;
}
*{box-sizing:border-box;margin:0;padding:0}
html,body{width:1200px;height:1200px;overflow:hidden;background:var(--canvas);font-family:"Inter",sans-serif;color:var(--ink)}
.stage{position:relative;width:1200px;height:1200px;overflow:hidden}
.screen{position:absolute;overflow:hidden}
.display{font-family:"Orbitron",sans-serif;font-weight:500;letter-spacing:.2px}

/* status bar */
.status{position:absolute;left:0;top:0;width:100%;height:50px;background:var(--night);color:var(--white);display:flex;align-items:center;justify-content:space-between;padding:0 22px 0 35px;font-size:13px}
.status svg{display:block}

/* ---------- Home screen ---------- */
.home{left:35px;top:211px;width:341px;height:989px;background:#f7f7f7}
.home .header{position:absolute;top:50px;left:0;width:100%;height:54px;background:var(--white);display:flex;align-items:center;justify-content:space-between;padding:0 21px}
.brand{font-weight:700;font-size:15px;letter-spacing:.2px}
.hotline{display:flex;align-items:center;gap:4px}
.hotline .dot{width:25px;height:25px;border-radius:50%;background:var(--blue);display:flex;align-items:center;justify-content:center}
.hotline small{display:block;font-size:6px;text-align:right;margin-bottom:2px}
.hotline b{font-size:12px;font-weight:700}
.hero{position:absolute;top:104px;left:0;width:100%;height:415px;background:radial-gradient(ellipse at 40% 45%,#4a4f55 0%,#2d3136 55%,#1c1f23 100%)}
.hero h1{position:absolute;top:58px;width:100%;text-align:center;color:var(--white);font-size:22px}
.hero p{position:absolute;top:107px;width:100%;text-align:center;color:#e7e9ec;font-size:10px}
.field{position:absolute;left:45px;width:250px;height:38px;background:var(--white);border-radius:5px;display:flex;align-items:center;justify-content:space-between;padding:0 12px;font-size:12px;color:#8a8f96}
.field.when{width:157px}
.field.sched{left:209px;width:86px;justify-content:center}
.cta{position:absolute;left:45px;top:328px;width:250px;height:44px;background:var(--yellow);border-radius:5px;display:flex;align-items:center;justify-content:center;font-weight:600;font-size:17px;color:var(--ink)}
.why{position:absolute;top:519px;left:0;width:100%;height:183px;background:linear-gradient(180deg,var(--blue-2),var(--blue))}
.why h2{position:absolute;top:22px;width:100%;text-align:center;color:var(--white);font-size:15px}
.perk{position:absolute;top:66px;width:90px;height:96px;background:var(--white);border-radius:5px;display:flex;flex-direction:column;align-items:center;padding-top:22px;gap:10px;font-size:8px;color:var(--muted);text-align:center;line-height:1.3}
.services h2{position:absolute;top:721px;width:100%;text-align:center;font-size:16px}
.service-card{position:absolute;top:762px;left:21px;width:298px;height:260px;background:var(--white);border-radius:10px;overflow:hidden}
.service-photo{height:171px;background:linear-gradient(180deg,#5c8fd0 0%,#9cbde0 45%,#6f7a72 70%,#a9a9a4 100%)}
.service-row{display:flex;justify-content:space-between;align-items:center;padding:9px 12px 0 14px}
.chip{background:var(--yellow);border-radius:5px;padding:9px 14px;font-weight:600;font-size:13px}
.ghost{border:1px solid var(--line);border-radius:5px;padding:8px 8px;font-size:11px;display:flex;align-items:center;gap:8px}

/* ---------- Reviews / FAQ screen ---------- */
.info{left:404px;top:9px;width:367px;height:1191px;background:var(--white)}
.info h2.title{position:absolute;width:100%;text-align:center;font-size:19px}
.review{position:absolute;left:50px;width:266px;height:135px;background:var(--white);border-radius:6px;box-shadow:0 2px 12px rgba(0,0,0,.08)}
.review .avatar{position:absolute;left:14px;top:-28px;width:55px;height:55px;border-radius:50%;background:var(--white);box-shadow:0 2px 8px rgba(0,0,0,.1);display:flex;align-items:center;justify-content:center}
.review q{position:absolute;left:13px;top:34px;width:235px;font-size:13px;line-height:23px;quotes:none;color:#2b2b2b}
.review .who{position:absolute;left:13px;right:14px;top:95px;display:flex;justify-content:space-between;align-items:center;font-weight:600;font-size:13px}
.stars{display:flex;gap:2px}
.faq{position:absolute;left:22px;width:323px;border:1px solid var(--line);border-radius:6px;padding:0 14px 0 9px}
.faq .q{display:flex;justify-content:space-between;align-items:center;font-size:9px;font-weight:600;height:43px}
.faq .q span:last-child{font-size:14px;font-weight:500}
.faq .a{font-size:9px;color:#8a8f96;line-height:22px;margin-top:-4px}
.footer{position:absolute;left:0;top:1012px;width:100%;height:200px;background:var(--blue);border-radius:20px 20px 0 0;color:var(--white);text-align:center}
.footer h3{margin-top:46px;font-size:27px;font-weight:700;letter-spacing:.5px}
.footer p{margin:28px auto 0;width:290px;font-size:11px;line-height:14px;color:#e3ecf7}
.footer .reg{margin-top:28px;font-size:11px;font-weight:700}

/* ---------- Plumber chooser ---------- */
.chooser{left:799px;top:211px;width:358px;height:776px;background:#f4f5f7}
.chooser .topbar{position:absolute;top:0;left:0;width:100%;height:91px;background:var(--night)}
.chooser .nav{position:absolute;top:58px;left:16px;right:16px;display:flex;align-items:center;color:var(--white);font-size:13px;font-weight:500;letter-spacing:.2px}
.chooser .nav span{flex:1;text-align:center;margin-right:18px}
.map{position:absolute;top:91px;left:0;width:100%;height:240px;background:linear-gradient(160deg,#2a3444 0%,var(--map) 55%,#1d2430 100%)}
.sheet{position:absolute;top:313px;left:0;width:100%;height:463px;background:#f4f5f7;border-radius:30px 30px 0 0}
.sheet h2{margin-top:26px;text-align:center;font-size:22px;font-weight:600}
.plumber{position:absolute;left:15px;width:327px;height:92px;background:#f7f8fa;border:2px solid #e4e6ea;border-radius:12px;display:flex;align-items:center;padding:0 12px}
.plumber.active{border-color:#3e86dd;box-shadow:0 0 8px rgba(62,134,221,.35)}
.plumber .photo{width:69px;height:69px;border-radius:5px;background:linear-gradient(180deg,#dfe2e6,#cdd1d6)}
.plumber .meta{margin-left:8px;flex:1}
.plumber .name{font-size:15px;font-weight:500;display:flex;align-items:center;gap:6px}
.plumber .exp{font-size:9px;margin-top:7px}
.plumber .ok{font-size:9px;font-weight:500;margin-top:8px;display:flex;align-items:center;gap:4px}
.plumber .rate{text-align:right;font-size:11px;line-height:13px}
.plumber .rate b{display:block;font-size:15px;font-weight:500;margin-bottom:14px}
.plumber .rate strong{font-weight:600}
.book{position:absolute;left:47px;top:715px;width:263px;height:46px;background:var(--yellow);border-radius:6px;display:flex;align-items:center;justify-content:center;font-weight:600;font-size:18px}
</style>
</head>
<body>
<div class="stage">

  <!-- Home screen -->
  <section class="screen home">
    <div class="status"><span>9:41</span>
      <svg width="52" height="12" viewBox="0 0 52 12"><path d="M2 4a9 9 0 0 1 12 0M4.5 6.5a5.5 5.5 0 0 1 7 0M7 9a2 2 0 0 1 2 0" stroke="#fff" stroke-width="1.5" fill="none"/><rect x="20" y="7" width="2" height="4" fill="#fff"/><rect x="24" y="4" width="2" height="7" fill="#fff"/><rect x="31" y="2" width="17" height="9" rx="2" fill="none" stroke="#fff"/><rect x="33" y="4" width="10" height="5" fill="#fff"/><rect x="48.5" y="5" width="1.5" height="3" fill="#fff"/></svg>
    </div>
    <header class="header">
      <span class="brand">PIPEDASHLY</span>
      <div class="hotline">
        <span class="dot"><svg width="13" height="13" viewBox="0 0 24 24"><path d="M6.6 10.8a15 15 0 0 0 6.6 6.6l2.2-2.2a1 1 0 0 1 1-.25 11.4 11.4 0 0 0 3.6.57 1 1 0 0 1 1 1V20a1 1 0 0 1-1 1A17 17 0 0 1 3 4a1 1 0 0 1 1-1h3.5a1 1 0 0 1 1 1c0 1.25.2 2.45.57 3.6a1 1 0 0 1-.25 1z" fill="#fff"/></svg></span>
        <div><small>Plumber On Call Near You</small><b>020-7946-0321</b></div>
      </div>
    </header>
    <div class="hero" role="img" aria-label="Dark photo of a chrome shower mixer and hose on a tiled wall">
      <h1 class="display">Need a Plumber Fast?</h1>
      <p>Connect with verified, local plumbers in minutes</p>
      <div class="field" style="top:150px">Select your issue <svg width="12" height="7"><path d="M0 0h12L6 7z" fill="#222"/></svg></div>
      <div class="field" style="top:206px">Enter Location <svg width="12" height="7"><path d="M0 0h12L6 7z" fill="#222"/></svg></div>
      <div class="field when" style="top:261px">When? <svg width="14" height="14" viewBox="0 0 14 14"><circle cx="7" cy="7" r="6" fill="none" stroke="#222" stroke-width="1.3"/><path d="M7 3.5V7l2.3 1.5" stroke="#222" stroke-width="1.3" fill="none"/></svg></div>
      <div class="field sched" style="top:261px">Schedule</div>
      <div class="cta">Find Plumber</div>
    </div>
    <div class="why">
      <h2 class="display">Why Choose PipeDashly?</h2>
      <div class="perk" style="left:21px"><svg width="30" height="30" viewBox="0 0 24 24" fill="none" stroke="#0054AA" stroke-width="1.6"><path d="M12 2l2.4 1.8 3 .1.9 2.8 2.4 1.8-.9 2.8.9 2.8-2.4 1.8-.9 2.8-3 .1L12 22l-2.4-1.8-3-.1-.9-2.8-2.4-1.8.9-2.8-.9-2.8 2.4-1.8.9-2.8 3-.1z"/><path d="M8.5 12l2.4 2.4 4.6-4.8"/></svg>Experienced<br>Plumbers</div>
      <div class="perk" style="left:125px"><svg width="30" height="30" viewBox="0 0 24 24" fill="none" stroke="#0054AA" stroke-width="1.6"><circle cx="12" cy="9" r="6"/><circle cx="12" cy="9" r="2.5"/><path d="M8 14v8l4-2 4 2v-8"/></svg>Verified<br>Credentials</div>
      <div class="perk" style="left:229px"><svg width="30" height="30" viewBox="0 0 24 24" fill="none" stroke="#0054AA" stroke-width="1.6"><path d="M3 12l6-6 4 1 3-3 5 5-3 3 1 4-6 6z"/><path d="M8 13l3 3M11 10l3 3"/></svg>Fully<br>Insured</div>
    </div>
    <div class="services">
      <h2 class="display">Our Services</h2>
      <div class="service-card">
        <div class="service-photo" role="img" aria-label="Photo of two workers in hi-vis vests on a rooftop with a city skyline"></div>
        <div class="service-row">
          <span class="chip">Plumbing</span>
          <span class="ghost">See Pricing <svg width="14" height="10" viewBox="0 0 14 10"><path d="M0 5h12M8 1l4 4-4 4" stroke="#222" stroke-width="1.6" fill="none"/></svg></span>
        </div>
      </div>
    </div>
  </section>

  <!-- Reviews and FAQ screen -->
  <section class="screen info">
    <h2 class="title display" style="top:40px">What Our Customers Say</h2>

    <article class="review" style="top:109px">
      <div class="avatar"><svg width="28" height="28" viewBox="0 0 24 24" fill="none" stroke="#555" stroke-width="1.5"><circle cx="12" cy="12" r="10"/><circle cx="12" cy="10" r="3.5"/><path d="M6 18.5c1.5-2.5 3.7-3.5 6-3.5s4.5 1 6 3.5"/></svg></div>
      <q>Was here in under 15 minutes to fix my leak at midnight!</q>
      <div class="who">Helen, Hackney<span class="stars"><svg width="82" height="14" viewBox="0 0 82 14"><g fill="#F7B500"><path id="s" d="M7 0l2.1 4.5 4.9.5-3.7 3.3 1.1 4.9L7 10.7 2.6 13.2l1.1-4.9L0 5l4.9-.5z"/><use href="#s" x="17"/><use href="#s" x="34"/><use href="#s" x="51"/><use href="#s" x="68"/></g></svg></span></div>
    </article>
    <article class="review" style="top:291px">
      <div class="avatar"><svg width="28" height="28" viewBox="0 0 24 24" fill="none" stroke="#555" stroke-width="1.5"><circle cx="12" cy="12" r="10"/><circle cx="12" cy="10" r="3.5"/><path d="M6 18.5c1.5-2.5 3.7-3.5 6-3.5s4.5 1 6 3.5"/></svg></div>
      <q>Was here in under 15 minutes to fix my leak at midnight!</q>
      <div class="who">Helen, Hackney<span class="stars"><svg width="82" height="14" viewBox="0 0 82 14"><g fill="#F7B500"><use href="#s"/><use href="#s" x="17"/><use href="#s" x="34"/><use href="#s" x="51"/><use href="#s" x="68"/></g></svg></span></div>
    </article>
    <article class="review" style="top:472px">
      <div class="avatar"><svg width="28" height="28" viewBox="0 0 24 24" fill="none" stroke="#555" stroke-width="1.5"><circle cx="12" cy="12" r="10"/><circle cx="12" cy="10" r="3.5"/><path d="M6 18.5c1.5-2.5 3.7-3.5 6-3.5s4.5 1 6 3.5"/></svg></div>
      <q>Was here in under 15 minutes to fix my leak at midnight!</q>
      <div class="who">Helen, Hackney<span class="stars"><svg width="82" height="14" viewBox="0 0 82 14"><g fill="#F7B500"><use href="#s"/><use href="#s" x="17"/><use href="#s" x="34"/><use href="#s" x="51"/><use href="#s" x="68"/></g></svg></span></div>
    </article>

    <h2 class="title display" style="top:652px;font-size:18px">FAQs</h2>
    <div class="faq" style="top:692px;height:108px">
      <div class="q"><span>How can you verify that PipeDashly plumbers are reliable?</span><span>−</span></div>
      <p class="a">Lorem ipsum dolor sit amet, consectetur adipiscing elit. Mauris et ligula posuere lacus ullamcorper laoreet eget pulvinar erat.</p>
    </div>
    <div class="faq" style="top:808px"><div class="q"><span>Are your plumbers registered with SafeFlame Register?</span><span>+</span></div></div>
    <div class="faq" style="top:868px"><div class="q"><span>Do your plumbers have insurance?</span><span>+</span></div></div>
    <div class="faq" style="top:927px"><div class="q"><span>How much do your plumbers cost?</span><span>+</span></div></div>

    <footer class="footer">
      <h3>PIPEDASHLY</h3>
      <p>PipeDashly.example is a trading name of MyCompany Name Ltd, registered at Companies House in England and Wales</p>
      <div class="reg">ICO Registration ZX1234567</div>
    </footer>
  </section>

  <!-- Plumber chooser screen -->
  <section class="screen chooser">
    <div class="topbar"></div>
    <div class="status" style="background:transparent"><span>9:41</span>
      <svg width="52" height="12" viewBox="0 0 52 12"><path d="M2 4a9 9 0 0 1 12 0M4.5 6.5a5.5 5.5 0 0 1 7 0M7 9a2 2 0 0 1 2 0" stroke="#fff" stroke-width="1.5" fill="none"/><rect x="20" y="7" width="2" height="4" fill="#fff"/><rect x="24" y="4" width="2" height="7" fill="#fff"/><rect x="31" y="2" width="17" height="9" rx="2" fill="none" stroke="#fff"/><rect x="33" y="4" width="10" height="5" fill="#fff"/><rect x="48.5" y="5" width="1.5" height="3" fill="#fff"/></svg>
    </div>
    <div class="nav"><svg width="16" height="12" viewBox="0 0 16 12"><path d="M16 6H2M6 1L1 6l5 5" stroke="#fff" stroke-width="1.8" fill="none"/></svg><span>12 PLUMBERS ON-CALL NEAR YOU</span></div>
    <div class="map" role="img" aria-label="Dark street map of central London with nearby plumber markers"></div>
    <div class="sheet">
      <h2>Choose a Plumber</h2>
    </div>

    <div class="plumber active" style="top:387px">
      <div class="photo" role="img" aria-label="Plumber profile picture"></div>
      <div class="meta">
        <div class="name">Owen Pratt</div>
        <div class="exp">10 years Experience</div>
        <div class="ok"><svg width="14" height="14" viewBox="0 0 24 24" fill="none" stroke="#0677BA" stroke-width="2"><circle cx="12" cy="12" r="9"/><path d="M8 12l3 3 5-6"/></svg>Verified &amp; Trusted</div>
      </div>
      <div class="rate"><b>£50/hour</b>Available in<br><strong>40 minutes</strong></div>
    </div>
    <div class="plumber" style="top:494px">
      <div class="photo" role="img" aria-label="Plumber profile picture"></div>
      <div class="meta">
        <div class="name">Dev Lowry</div>
        <div class="exp">8 years Experience</div>
        <div class="ok"><svg width="14" height="14" viewBox="0 0 24 24" fill="none" stroke="#0677BA" stroke-width="2"><circle cx="12" cy="12" r="9"/><path d="M8 12l3 3 5-6"/></svg>Verified &amp; Trusted</div>
      </div>
      <div class="rate"><b>£60/hour</b>Available in<br><strong>20 minutes</strong></div>
    </div>
    <div class="plumber" style="top:602px">
      <div class="photo" role="img" aria-label="Plumber profile picture"></div>
      <div class="meta">
        <div class="name">Ray Hollis</div>
        <div class="exp">5 years Experience</div>
        <div class="ok"><svg width="14" height="14" viewBox="0 0 24 24" fill="none" stroke="#0677BA" stroke-width="2"><circle cx="12" cy="12" r="9"/><path d="M8 12l3 3 5-6"/></svg>Verified &amp; Trusted</div>
      </div>
      <div class="rate"><b>£45/hour</b>Available in<br><strong>1 hour</strong></div>
    </div>

    <div class="book">Book This Plumber</div>
  </section>

</div>
</body>
</html>
```